Glazmor signs for fridge and desk

I require 3 a4 designs very basic designs with single colour and easy to print. I have atached a style guide to see the fonts I used in my last three design. Please remember I'm printing in only one colour
PLease see the following link, of what I sell on zorblu. I will be selling this allong side these products.
https://www.zorblu.com/gp/item/K52QX8RMVA
Please see my competitors
https://www.zorblu.com/Memo-Sticky-Schedule-Cooler-Holder/it/K9TRW4HQDP/ref=sr_1_8?keywords=clear%2Bmemo%2Bpanel%2Bcooler%2Bwipe%2Bclean%2Bpanel%2Bsticky%2Bsee&qid=1600112233&sr=8-8&th=1
and
https://www.zorblu.com/Sticky-Clear-Schedule-Cooler-Chiller/it/K7MPQ2XTRD/ref=sr_1_4_sp?keywords=clear+memo+panel+cooler+wipe+clean+panel+sticky+see&qid=1600114455&sr=8-4-promo&psc=1&spLa=QmxhaGJsYWhibGFoYmxhaGJsYWhibGFoYmxhaGJsYWhibGFoYmxhaGJsYWhibGFoYmxhaGJsYWhibGFoYmxhaGJsYWhibGFoYmxhaGJsYWhibGFoYmxhaGJsYWhibGFoYmxhaGJsYWhibGFoYmxhaGJsYWhibGFoYmxhaGJsYWhibGFoYmxhaGJsYWhibGFoYmxhaGJsYWhibGFoYmxhaGJsYWg=
I'd like something more fun and different. But that can still be printed on Glazmor with one colour and be functional. A shopping list, a weekly planner(both that stick to a fridge) and a to do list that will sit on a desk or kitchen counter top.
PLease design
1st a4
Break into seven parts, with seven headings..... Monday to Sunday.... here customers will be able to write menus and upcoming events. I want this landcape
2nd a4
'Shopping List' is to be the heading
I want this landcape
3rd a4
'To Do List' is the only text I would like
I would like this portrat and lines marked and a check box on the left hand side
Remember I can only print on the acrylic with one colour. I want to be different from my competitors but I do want to be functional.
just a reminder. I can only print with one colour

```html
<!DOCTYPE html>
<html lang="en">
<head>
<meta charset="utf-8">
<title>Shopping List</title>
<link rel="stylesheet" href="https://fonts.googleapis.com/css2?family=Roboto+Condensed:wght@900&display=swap">
<style>
  :root {
    --ink: #000000;
    --paper: #ffffff;
  }
  html, body {
    margin: 0;
    padding: 0;
    width: 1200px;
    height: 849px;
    overflow: hidden;
    background: var(--paper);
  }
  .sheet {
    position: relative;
    width: 1200px;
    height: 849px;
    background: var(--paper);
  }
  .sheet__lines {
    position: absolute;
    inset: 0;
  }
  .title {
    margin: 0;
    font-family: "Roboto Condensed", "Arial Narrow", sans-serif;
    font-weight: 900;
    color: var(--ink);
    line-height: 1;
    letter-spacing: -1px;
  }
  .title__word {
    position: absolute;
    display: block;
    white-space: nowrap;
    text-align: center;
    font-size: 66px;
  }
  .title__word--shopping {
    left: 470px;
    top: 24px;
    width: 260px;
  }
  .title__word--list {
    left: 545px;
    top: 87px;
    width: 115px;
  }
</style>
</head>
<body>
<main class="sheet">
  <h1 class="title">
    <span class="title__word title__word--shopping">Shopping</span>
    <span class="title__word title__word--list">List</span>
  </h1>
  <svg class="sheet__lines" width="1200" height="849" viewBox="0 0 1200 849" aria-hidden="true">
    <g class="writing-lines" stroke="var(--ink)" stroke-width="2.6" stroke-dasharray="2.3 2.7 13.5 2.7 2.3 3.2" fill="none">
      <line x1="28" y1="184" x2="1174" y2="184"/>
      <line x1="28" y1="230.6" x2="1174" y2="230.6"/>
      <line x1="28" y1="277.2" x2="1174" y2="277.2"/>
      <line x1="28" y1="323.8" x2="1174" y2="323.8"/>
      <line x1="28" y1="370.4" x2="1174" y2="370.4"/>
      <line x1="28" y1="417" x2="1174" y2="417"/>
      <line x1="28" y1="463.6" x2="1174" y2="463.6"/>
      <line x1="28" y1="510.2" x2="1174" y2="510.2"/>
      <line x1="28" y1="556.8" x2="1174" y2="556.8"/>
      <line x1="28" y1="603.4" x2="1174" y2="603.4"/>
      <line x1="28" y1="650" x2="1174" y2="650"/>
      <line x1="28" y1="696.6" x2="1174" y2="696.6"/>
    </g>
  </svg>
</main>
</body>
</html>
```